Business card design needed

the business is HR Consulting, but its for SME businesses who cant afford a permanent HR person. We sell an HR info system to help them meet minimum employment legislation but with this hope they then require us on a monthly subscription to phone or email us for HR advice. We are HR qualified mums working from home

So we will be partners to HR and Payroll systems known as kindle HR and Pluto

Target Market(s)

Small to medium businesses so not black and overly corporate, but having said that many are accounting businesses

Industry/Entity Type

Business

Contact Information for Business Card

Name of the company: Tandem HR

Me:Marta Kovalenko
Title:Managing Director

m: 0437 215 683
e: marta@tandemhr.com.au
w: www.tandemhr.com.au

What we do: HR Consulting, HR Systems and support, Payroll Advice

Requirements
Nice to have
• there is a company already out there known as Quartz professionals. I like the leaves at the end as I wanted something different like this to the usual business logos but still professional. I wanted a symbol to show calm, positive, ease flow going up ,etc. but realise they have the leaves and possibly cant copy, or can we?..( kite??, something calm and positive)dont know!!. Green and blue needed to be in it as nature and calm as well. I love the colours of www.stafflanefund.com ( attached the colours), as well as the calm wave line underneath. have a look as while they use green and blue I loved the purple colour thrown in there.Green and blue on their own are so overused. I want vibrant. I want double sided and when on a table I want it to stand out so maybe the purple colour (as per the colours on the fund website) solid on one side with just the 3 services we provide and personal and company name on front but need some creativity from you guys.

```html
<!DOCTYPE html>
<html lang="en">
<head>
<meta charset="utf-8">
<title>Tandem HR – Business Card</title>
<link rel="stylesheet" href="https://fonts.googleapis.com/css2?family=Questrial&display=swap">
<style>
  :root {
    --backdrop: #e4e4e6;
    --card: #ffffff;
    --purple: #9b3a9a;
    --teal: #2a9fae;
  }
  html, body {
    margin: 0;
    padding: 0;
    width: 1200px;
    height: 900px;
    overflow: hidden;
    background: var(--backdrop);
  }
  .canvas {
    position: relative;
    width: 1200px;
    height: 900px;
    font-family: "Questrial", "Century Gothic", sans-serif;
  }
  .business-card {
    position: absolute;
    left: 150px;
    top: 193px;
    width: 900px;
    height: 514px;
    background: var(--card);
    box-shadow: 0 10px 30px rgba(0, 0, 0, 0.18);
    box-sizing: border-box;
    padding: 86px 70px 0;
  }
  .brand-name {
    margin: 0;
    font-size: 78px;
    font-weight: 400;
    line-height: 1;
    color: var(--purple);
    letter-spacing: -1px;
  }
  .services {
    margin: 22px 0 0;
    font-size: 21px;
    color: var(--teal);
  }
  .person-name {
    margin: 52px 0 0;
    font-size: 36px;
    font-weight: 400;
    color: var(--purple);
  }
  .person-title {
    margin: 4px 0 0;
    font-size: 22px;
    color: var(--teal);
  }
  .contact {
    margin: 36px 0 0;
    padding: 0;
    list-style: none;
    font-size: 22px;
    line-height: 1.4;
  }
  .contact-label { color: var(--purple); }
  .contact-value { color: var(--teal); }
</style>
</head>
<body>
<main class="canvas">
  <section class="business-card" aria-label="Tandem HR business card">
    <p class="brand-name">Tandem HR</p>
    <p class="services">HR Consulting, HR Systems and support, Payroll Advice</p>
    <h1 class="person-name">Marta Kovalenko</h1>
    <p class="person-title">Managing Director</p>
    <ul class="contact">
      <li>
        <span class="contact-label">m:</span> <span class="contact-value">0437 215 683</span>
        <span class="contact-label">e:</span> <span class="contact-value">marta@tandemhr.com.au</span>
      </li>
      <li>
        <span class="contact-label">w:</span> <span class="contact-value">www.tandemhr.com.au</span>
      </li>
    </ul>
  </section>
</main>
</body>
</html>
```